TalvenInsight card back

Our company already has a logo and we have business cards. (I have included a picture of my business card front that i plan to use.) I want to promote a new division of Talven, called "TalvenInsight" and would like the back side of my card designed to promote this division using the same color scheme and concept as front. So I'm looking for a design for the TalvenInsight (back) side of my card. This back side does need any contact info - including that it doesn't need my name, phone, email etc. I have included the tag line that I would like to have included on that TalvenInsight side of the card. But i'd like the design to reflect "wisdom" but using a similar theme as in our sun logo. One concept i have for this side of the card has the sun is entirely out of the box and lighting up a spacious blue background to the card. Then there's a "TalvenInsight" as well as the tag line. I welcome concepts along these lines or others that you may have. Thanks!

Target Market(s)

High-end energy, or technology firms. Business leaders within the firm.

Industry/Entity Type

Professional Service

Contact Information for Business Card

The card will be double sided, but i only the need the single TalvenInsight side designed. It has to coordinate with the front side (I've included a picture of it) in color, etc.

Logo Text

TalvenInsight

Font styles to use
Other font styles liked:
• font from existing card front

Requirements
Must have
• The tie in with the Talven sun from our logo. A sense of spaciousness and/or clarity that comes from enlightened wisdom. A professional feel but a feel good feel too. The division label "TalvenInsight" and in a similar font as the existing business card. The tag line.
Should not have
• The back, TalvenINsight, side should not have contact info and should not repeat any of the front side info, given that it will be printed on the back side of card.

```html
<!DOCTYPE html>
<html lang="en">
<head>
<meta charset="utf-8">
<title>TalvenInsight business cards</title>
<link rel="stylesheet" href="https://fonts.googleapis.com/css2?family=Gelasio:wght@400&family=Roboto:wght@400;500;700&family=Arimo:wght@400;700&display=swap">
<style>
  :root {
    --backdrop: #e6e6e6;
    --card: #f7f7f6;
    --navy: #1f3766;
    --ink: #1c1c1c;
    --grey-text: #8a8a8a;
    --dark-text: #3c3c3c;
    --orange: #e8731b;
    --sun: rgba(249, 224, 166, 0.8);
    --sun-mid: rgba(249, 224, 166, 0.45);
    --sun-soft: rgba(249, 224, 166, 0);
  }
  * { margin: 0; padding: 0; box-sizing: border-box; }
  html, body { width: 1200px; height: 576px; overflow: hidden; }
  body { background: var(--backdrop); position: relative; }

  .card {
    position: absolute;
    top: 138px;
    width: 484px;
    height: 294px;
    background: var(--card);
    border-radius: 13px;
    overflow: hidden;
    box-shadow: 2px 4px 6px rgba(0,0,0,0.25);
  }
  .card--insight { left: 82px; }
  .card--contact { left: 602px; width: 481px; height: 291px; }

  .sun-glow {
    position: absolute;
    width: 360px;
    height: 360px;
    border-radius: 50%;
    background: radial-gradient(circle, var(--sun) 0%, var(--sun) 34%, var(--sun-mid) 52%, var(--sun-soft) 72%);
  }
  .card--insight .sun-glow { left: -82px; top: -74px; }
  .card--contact .sun-glow { left: -78px; top: -74px; }

  .wordmark {
    position: absolute;
    display: flex;
    align-items: center;
    font-family: "Gelasio", Georgia, serif;
    font-weight: 400;
    color: var(--navy);
    line-height: 1;
  }
  .wordmark__square { display: block; background: var(--navy); flex: none; }

  .card--insight .wordmark { left: 42px; top: 90px; gap: 30px; font-size: 52px; }
  .card--insight .wordmark__square { width: 48px; height: 52px; }

  .tagline {
    position: absolute;
    left: 0; right: 0; top: 217px;
    text-align: center;
    font-family: "Roboto", Arial, sans-serif;
    font-size: 13px;
    line-height: 16px;
    color: var(--ink);
  }
  .tagline strong { font-weight: 500; }

  .definition {
    position: absolute;
    left: 19px; top: 58px;
    width: 190px;
    font-family: "Arimo", Arial, sans-serif;
    font-size: 13px;
    line-height: 15.4px;
    color: var(--dark-text);
  }
  .definition__word { font-weight: 700; color: var(--ink); }
  .definition__origin { font-style: italic; color: var(--grey-text); }
  .definition__muted { color: var(--grey-text); }

  .card--contact .wordmark { left: 224px; top: 44px; gap: 18px; font-size: 42px; letter-spacing: 0.5px; }
  .card--contact .wordmark__square { width: 46px; height: 44px; }

  .person {
    position: absolute;
    left: 224px; top: 134px;
    font-family: "Roboto", Arial, sans-serif;
    color: var(--navy);
  }
  .person__name { font-size: 17px; font-weight: 500; line-height: 20px; }
  .person__title { font-size: 13px; line-height: 17px; margin-top: 1px; }
  .person__details { margin-top: 9px; font-size: 11.2px; line-height: 15.8px; }
  .person__web { color: var(--orange); }
</style>
</head>
<body>
  <section class="card card--insight" aria-label="TalvenInsight card side">
    <div class="sun-glow" role="img" aria-label="Faint pale-yellow sun decoration"></div>
    <div class="wordmark">
      <span class="wordmark__square"></span>
      <span class="wordmark__name">TalvenInsight</span>
    </div>
    <p class="tagline">
      <strong>Talven + Insight = TalvenInsight</strong><br>
      Offering Vision, Creativity and Resilience to<br>
      Individuals and Organizations
    </p>
  </section>

  <section class="card card--contact" aria-label="Talven contact card side">
    <div class="sun-glow" role="img" aria-label="Faint pale-yellow sun decoration"></div>
    <p class="definition">
      <span class="definition__word">talven</span> <span class="definition__origin">&lt;Latin: to reveal&gt;</span><br>
      <span class="definition__muted">1. To unlock, unclose;<br>to lay open;</span> 2. To bring,<br>
      clarity, focus, purpose,<br>
      and leadership to critical<br>
      electric industry matters
    </p>
    <div class="wordmark">
      <span class="wordmark__square"></span>
      <span class="wordmark__name">TALVEN</span>
    </div>
    <div class="person">
      <p class="person__name">Mara Quinlan</p>
      <p class="person__title">President</p>
      <p class="person__details">
        O: 916-555-0142 | M: 916-555-0178<br>
        F: 916-555-0190 | mquinlan@talven.co<br>
        <span class="person__web">www.talven.com</span><br>
        4170 Cedar Hollow Lane<br>
        Alder Ridge, CA 95702
      </p>
    </div>
  </section>
</body>
</html>
```